Meridale Cleaning Services

In need of a business card design suited for a growing cleaning company.

We offer our cleaning and maintenance services to a wide range of clients including but not limited to the following: constuction industry, hospitality, commercial, industrial and domestic

I want the card to be very noticable, i would like people to say 'hey, great card!' when i hand them my card.double sided would be nice

we want our business to come across as exceedingly professional and innovative (different).

a contemporary design is what we have in mind
we want to present an image of a quality business with a high standard of excellence in consistent service.

i just really need a card that persuades top end quality,
our business is very certified and also strives towards environmentaly friendly alternatives
Updates

hey sorry, i have uploaded my company logo design and name
cheers.

hey guys i have added my company logo/name file on my brief page. many thanks

sorry guys a typo in the brief..
address is Tolley Rd. not Tolly Rd
thanks

Industry/Entity Type

Industrial

Requirements
Must have
• company name: meridale cleaning services
operations manager: Colm Varetti
Tel: (02)9373 6204
Fax: (02)8645 7712
Mob: 0438571490

address: 47 Tolly RD Pymble NSW 2073
Postal Adress: PO Box 5832 North Ryde NSW 2113
email: meridaleclean@wexanet.com.au
website: meridalecleaningservices.com.au

```html
<!DOCTYPE html>
<html lang="en">
<head>
<meta charset="utf-8">
<title>Meridale Cleaning Services – Business Card Options</title>
<link rel="stylesheet" href="https://fonts.googleapis.com/css2?family=Open+Sans:wght@400;600&family=Saira+Condensed:wght@300;400&display=swap">
<style>
  :root {
    --sheet: #ffffff;
    --ink: #1a1a1a;
    --card-dark: #262626;
    --card-darker: #1c1c1c;
    --brand-blue: #1f8fd6;
    --brand-blue-deep: #0b6fb5;
    --brand-green: #7cc21a;
    --brand-green-soft: #a6d944;
    --text-light: #e6e6e6;
    --mark-grey: #3b4752;
  }
  * { margin: 0; padding: 0; box-sizing: border-box; }
  html, body { width: 1200px; height: 1200px; overflow: hidden; background: var(--sheet); }
  body { position: relative; font-family: "Open Sans", Arial, sans-serif; color: var(--ink); }

  .option-title, .side-label {
    position: absolute; text-align: center; font-weight: 400; color: var(--ink);
  }
  .option-title { left: 0; width: 1200px; font-size: 42px; line-height: 1; }
  .side-label { width: 420px; font-size: 40px; line-height: 1; }

  .divider { position: absolute; left: 60px; top: 545px; width: 1060px; height: 3px; background: var(--ink); }

  .card {
    position: absolute; width: 420px; height: 240px; overflow: hidden;
    background: radial-gradient(ellipse at 60% 50%, #3a3a3a 0%, var(--card-dark) 55%, var(--card-darker) 100%);
  }
  .card--textured {
    background:
      repeating-linear-gradient(92deg, rgba(255,255,255,0.025) 0 2px, rgba(0,0,0,0.05) 2px 5px),
      radial-gradient(ellipse at 60% 50%, #2e2e2e 0%, #1e1e1e 60%, #151515 100%);
  }
  .card svg.waves { position: absolute; inset: 0; }

  .front-brand { position: absolute; left: 20px; top: 48px; display: flex; align-items: center; gap: 14px; }
  .front-brand__dot { width: 108px; height: 108px; border-radius: 50%; background: var(--brand-blue); flex: none; }
  .front-brand__name {
    font-family: "Open Sans", Arial, sans-serif; font-weight: 600; color: var(--brand-blue);
    font-size: 40px; line-height: 1.05;
  }
  .card--textured .front-brand__dot, .card--textured .front-brand__name { opacity: 0.85; }

  .back-mark {
    position: absolute; left: -10px; top: 56px; width: 132px; height: 132px; border-radius: 50%;
    background: var(--mark-grey);
  }

  .contact { position: absolute; left: 193px; top: 22px; right: 0; color: var(--text-light); }
  .contact__name {
    font-family: "Saira Condensed", "Arial Narrow", sans-serif; font-weight: 400;
    font-size: 27px; letter-spacing: 3px; color: var(--brand-blue); line-height: 1;
    padding-bottom: 4px; border-bottom: 1px solid var(--brand-blue);
  }
  .contact__role {
    font-family: "Saira Condensed", "Arial Narrow", sans-serif; font-weight: 300;
    font-size: 17px; letter-spacing: 3px; color: var(--brand-green); margin-top: 4px; line-height: 1;
  }
  .contact__group { font-size: 10.5px; line-height: 14px; margin-top: 16px; }
  .contact__group + .contact__group { margin-top: 14px; }
</style>
</head>
<body>

  <h2 class="option-title" style="top:80px;">Business Card # 1</h2>
  <p class="side-label" style="left:118px; top:194px;">Front</p>
  <p class="side-label" style="left:628px; top:190px;">Back</p>

  <!-- Option 1 front -->
  <div class="card" style="left:118px; top:264px;">
    <svg class="waves" viewBox="0 0 420 240" width="420" height="240" aria-hidden="true">
      <defs>
        <linearGradient id="greenSwoop1" x1="0" y1="0" x2="1" y2="0">
          <stop offset="0" stop-color="#7cc21a"/><stop offset="1" stop-color="#a6d944"/>
        </linearGradient>
        <linearGradient id="blueWave1" x1="0" y1="0" x2="1" y2="1">
          <stop offset="0" stop-color="#1f8fd6"/><stop offset="1" stop-color="#0b6fb5"/>
        </linearGradient>
      </defs>
      <path d="M190,0 C260,14 320,34 420,26 L420,0 Z" fill="url(#greenSwoop1)"/>
      <path d="M0,180 C60,140 120,240 250,224 C330,214 360,150 420,158 L420,240 L0,240 Z" fill="url(#blueWave1)"/>
    </svg>
    <div class="front-brand">
      <span class="front-brand__dot"></span>
      <span class="front-brand__name">Meridale<br>Cleaning Services</span>
    </div>
  </div>

  <!-- Option 1 back -->
  <div class="card" style="left:628px; top:264px;">
    <span class="back-mark"></span>
    <div class="contact">
      <p class="contact__name">Colm Varetti</p>
      <p class="contact__role">Operations Manager</p>
      <p class="contact__group">47 Tolley Rd . Pymble NSW 2073<br>PO Box 5832 North Ryde NSW 2113</p>
      <p class="contact__group">meridaleclean@wexanet.com.au<br>meridalecleaningservices.com.au</p>
      <p class="contact__group">Tel: (02)9373 6204<br>Fax: (02)8645 7712<br>Mob: 0438571490</p>
    </div>
  </div>

  <div class="divider"></div>

  <h2 class="option-title" style="top:608px;">Business Card # 2</h2>
  <p class="side-label" style="left:118px; top:690px;">Front</p>
  <p class="side-label" style="left:628px; top:686px;">Back</p>

  <!-- Option 2 front -->
  <div class="card card--textured" style="left:118px; top:761px;">
    <svg class="waves" viewBox="0 0 420 240" width="420" height="240" aria-hidden="true">
      <defs>
        <linearGradient id="greenSwoop2" x1="0" y1="0" x2="1" y2="0">
          <stop offset="0" stop-color="#6aa817"/><stop offset="1" stop-color="#8fc23a"/>
        </linearGradient>
        <linearGradient id="blueWave2" x1="0" y1="0" x2="1" y2="1">
          <stop offset="0" stop-color="#1a78b4"/><stop offset="1" stop-color="#0d5a92"/>
        </linearGradient>
      </defs>
      <path d="M190,0 C260,14 320,34 420,26 L420,0 Z" fill="url(#greenSwoop2)"/>
      <path d="M0,180 C60,140 120,240 250,224 C330,214 360,150 420,158 L420,240 L0,240 Z" fill="url(#blueWave2)"/>
    </svg>
    <div class="front-brand">
      <span class="front-brand__dot"></span>
      <span class="front-brand__name">Meridale<br>Cleaning Services</span>
    </div>
  </div>

  <!-- Option 2 back -->
  <div class="card card--textured" style="left:628px; top:761px;">
    <span class="back-mark"></span>
    <div class="contact">
      <p class="contact__name">Colm Varetti</p>
      <p class="contact__role">Operations Manager</p>
      <p class="contact__group">47 Tolley Rd . Pymble NSW 2073<br>PO Box 5832 North Ryde NSW 2113</p>
      <p class="contact__group">meridaleclean@wexanet.com.au<br>meridalecleaningservices.com.au</p>
      <p class="contact__group">Tel: (02)9373 6204<br>Fax: (02)8645 7712<br>Mob: 0438571490</p>
    </div>
  </div>

</body>
</html>
```